Flyer für Selbstwert-Coachin und Bewusstseinstrainerin
Der Flyer ist wunderschön, kreativ und edel geworden und wurde von der Designerin genau nach meinen Wünschen super umgesetzt! Ich bin sehr zufrieden und kann die Designerin Lunea2281 jedem nur empfehlen. Einfach Top!!! 1 A!!! Vielen herzlichen Dank!
Zielgruppe
Ich bin Selbstwert Coach und Bewusstseinstrainerin und möchte einen Flyer für mein neues Angebot 'Innenkraft Akademie für Jugendliche ab 16' gestalten lassen.
Die Zielgruppe sind Eltern von Jugendlichen in der Oberstufe, deren Kinder unter Schulstress und Leistungsdruck leiden und zu wenig Selbstbewusstsein haben.
Aufgabenstellung
Ich habe bereits das Titelbild bei Bildquell gesucht #739201584, bitte dieses nehmen, es kann auch ein ähnliches noch besseres vorgeschlagen werden.
Ich möchte einen ansprechenden, schönen, hochwertigen Flyer mit den Farben der Landingpage, gelb, blau, gold... und Bilder von Jugendlichen, dort wo Platz ist, ansprechend und klar. Bitte keine Schnörkel und 08 15 Figuren, das Auge soll hängen bleiben, der Flyer hängt straßenseitig. Dieser soll ein 6-seitiger Wickelfalz sein.

```html
<!DOCTYPE html>
<html lang="de">
<head>
<meta charset="utf-8">
<title>Innenkraft Akademie – Flyer</title>
<link href="https://fonts.googleapis.com/css2?family=Oswald:wght@500;600;700&family=Open+Sans:ital,wght@0,400;0,600;0,700;1,600&display=swap" rel="stylesheet">
<style>
  :root {
    --navy: #1c1c6b;
    --navy-deep: #14145a;
    --yellow: #f7c61a;
    --gold: #d9a21f;
    --gold-light: #f6e4a6;
    --ink: #3a3a4a;
    --paper: #ffffff;
    --stage: #d6d6d8;
  }
  * { box-sizing: border-box; margin: 0; padding: 0; }
  html, body { width: 1200px; height: 960px; overflow: hidden; }
  body { background: var(--stage); font-family: "Open Sans", sans-serif; color: var(--ink); }

  .flyer {
    position: absolute; left: 40px; top: 84px;
    width: 1120px; height: 792px;
    display: flex; background: var(--paper);
    box-shadow: 0 10px 30px rgba(0,0,0,.18);
  }
  .panel { position: relative; width: 373.33px; height: 100%; overflow: hidden; }

  /* Panel 1 – Vorteile */
  .benefit-photo {
    height: 170px;
    background: linear-gradient(135deg, #eef2f7 0%, #cfdbe8 55%, #e9d9c6 100%);
  }
  .panel-body { padding: 22px 30px 0 30px; }
  .section-title {
    font-family: "Oswald", sans-serif; font-weight: 700; color: var(--navy);
    text-transform: uppercase; line-height: 1.05;
  }
  .section-title.large { font-size: 32px; margin-bottom: 14px; }
  .section-title.medium { font-size: 24px; margin: 22px 0 10px; }
  .benefit-list { list-style: none; }
  .benefit-list li {
    display: flex; gap: 8px; font-size: 12.5px; line-height: 1.4; margin-bottom: 7px;
  }
  .benefit-list svg { flex: 0 0 14px; margin-top: 3px; }
  .requirements { font-size: 12.5px; line-height: 1.5; }

  /* Panel 2 – Kontakt */
  .contact { height: 240px; padding: 24px 0 0 0; }
  .contact-label {
    margin-left: 30px; width: 300px; padding: 10px 16px;
    background: linear-gradient(90deg, var(--navy-deep) 0%, var(--navy) 50%, #ffffff 100%);
    font-family: "Oswald", sans-serif; font-weight: 700; font-size: 22px; line-height: 1.1;
    color: var(--yellow); text-transform: uppercase;
  }
  .contact-details { padding: 16px 30px 0 46px; }
  .contact-name { font-weight: 700; font-size: 20px; color: var(--navy); }
  .contact-role { font-size: 11.5px; margin-bottom: 10px; }
  .contact-line { font-size: 12px; line-height: 1.55; }
  .contact-line b { color: var(--navy); display: inline-block; width: 52px; }

  .portrait-area {
    height: 240px; background: var(--yellow);
    display: flex; align-items: center; justify-content: center;
  }
  .portrait {
    width: 190px; height: 190px; border-radius: 50%;
    border: 6px solid #ffffff;
    background: radial-gradient(circle at 50% 40%, #e9cfa6 0%, #b89a6c 45%, #5f7a5a 100%);
  }
  .brand {
    height: 232px; display: flex; align-items: center; justify-content: center;
  }
  .brand-name {
    font-family: "Open Sans", sans-serif; font-weight: 600; font-size: 20px;
    color: var(--gold); letter-spacing: .5px;
  }
  .gold-band {
    position: absolute; left: 0; bottom: 0; width: 100%; height: 80px;
    background: linear-gradient(180deg, var(--gold) 0%, var(--yellow) 45%, var(--gold-light) 100%);
  }

  /* Panel 3 – Titel */
  .cover-photo {
    position: absolute; left: 0; top: 0; width: 100%; height: 340px;
    background: linear-gradient(160deg, #a8b98a 0%, #c9a27a 45%, #6d4a32 100%);
  }
  .cover-band { position: absolute; left: 0; top: 250px; width: 100%; height: 130px; }
  .cover-title {
    position: absolute; left: 26px; top: 290px; color: var(--yellow);
    font-family: "Oswald", sans-serif; font-weight: 700; font-size: 34px; line-height: 1;
    text-transform: uppercase;
  }
  .cover-title small {
    font-family: "Open Sans", sans-serif; font-weight: 600; font-size: 12px;
    text-transform: none; color: #ffffff; margin-left: 6px;
  }
  .cover-text { position: absolute; left: 30px; right: 28px; top: 410px; font-size: 14px; line-height: 1.45; }
  .cover-text p { margin-bottom: 14px; }
  .cover-text .lead { font-weight: 600; color: var(--navy); }
  .cover-footer {
    position: absolute; left: 0; bottom: 0; width: 100%; height: 118px;
    background: var(--navy); border-top: 8px solid var(--gold);
    padding: 20px 30px; color: var(--gold-light);
    font-style: italic; font-weight: 600; font-size: 15px; line-height: 1.45;
  }
</style>
</head>
<body>
<main class="flyer">

  <section class="panel panel-benefits">
    <div class="benefit-photo" role="img" aria-label="Foto: Hand setzt Holzwürfel mit Gesundheitssymbolen"></div>
    <div class="panel-body">
      <h2 class="section-title large">Vorteile und Nutzen</h2>
      <ul class="benefit-list">
        <li><svg width="14" height="14" viewBox="0 0 14 14"><path d="M1 7l4 4 8-9" fill="none" stroke="#1c1c6b" stroke-width="2.4"/></svg>Beste Prävention für die psychische Gesundheit, Steigerung des Wohlbefindens von Geist, Körper und Seele</li>
        <li><svg width="14" height="14" viewBox="0 0 14 14"><path d="M1 7l4 4 8-9" fill="none" stroke="#1c1c6b" stroke-width="2.4"/></svg>Konkrete Lösungsansätze bei auftretenden Konflikten, Schulproblemen und Mobbing</li>
        <li><svg width="14" height="14" viewBox="0 0 14 14"><path d="M1 7l4 4 8-9" fill="none" stroke="#1c1c6b" stroke-width="2.4"/></svg>Veränderter Umgang bzw. Reduktion von Überforderung, Leistungsdruck und Schulstress</li>
        <li><svg width="14" height="14" viewBox="0 0 14 14"><path d="M1 7l4 4 8-9" fill="none" stroke="#1c1c6b" stroke-width="2.4"/></svg>Persönlichkeitsentwicklung, Lernen fürs Leben</li>
        <li><svg width="14" height="14" viewBox="0 0 14 14"><path d="M1 7l4 4 8-9" fill="none" stroke="#1c1c6b" stroke-width="2.4"/></svg>Grundlagen zur Gestaltung eines glücklichen, erfolgreichen Lebens</li>
        <li><svg width="14" height="14" viewBox="0 0 14 14"><path d="M1 7l4 4 8-9" fill="none" stroke="#1c1c6b" stroke-width="2.4"/></svg>Stärkung von Selbstbewusstsein, Selbstvertrauen, Selbstliebe und Selbstwert</li>
      </ul>
      <h2 class="section-title medium">Voraussetzungen für<br>die Teilnahme</h2>
      <p class="requirements">Das Wichtigste ist, dass dein Kind am Lehrgang teilnehmen will. Interesse, Neugierde und vor allem die Bereitschaft zur aktiven Umsetzung der Inhalte sind notwendig, um gute Ergebnisse zu erzielen.</p>
    </div>
  </section>

  <section class="panel panel-contact">
    <div class="contact">
      <div class="contact-label">Kontakt &amp;<br>Veranstalterin:</div>
      <div class="contact-details">
        <p class="contact-name">Mag. Clara Hollenstein</p>
        <p class="contact-role">Selbstwert Coach, Bewusstseinstrainerin</p>
        <p class="contact-line"><b>E-Mail:</b>info@innenkraft-coaching.at</p>
        <p class="contact-line"><b>Mobil:</b>+43(0)660 412 7780</p>
      </div>
    </div>
    <div class="portrait-area">
      <div class="portrait" role="img" aria-label="Porträtfoto der Veranstalterin"></div>
    </div>
    <div class="brand">
      <span class="brand-name">Clara Hollenstein</span>
    </div>
    <div class="gold-band"></div>
  </section>

  <section class="panel panel-cover">
    <div class="cover-photo" role="img" aria-label="Foto: jubelnde Jugendliche mit lockigem Haar"></div>
    <svg class="cover-band" viewBox="0 0 373 130" preserveAspectRatio="none">
      <defs>
        <linearGradient id="bandGold" x1="0" x2="1">
          <stop offset="0" stop-color="#f6e4a6"/><stop offset="1" stop-color="#d9a21f"/>
        </linearGradient>
      </defs>
      <polygon points="0,30 373,0 373,110 0,110" fill="#1c1c6b"/>
      <rect x="0" y="110" width="373" height="20" fill="url(#bandGold)"/>
    </svg>
    <h1 class="cover-title">Innenkraft<br>Akademie<small>für Jugendliche ab 16</small></h1>
    <div class="cover-text">
      <p class="lead">Schulbegleitender Praxis Lehrgang für mentale Stärke und Selbstbewusstsein</p>
      <p>Schulstress &amp; Leistungsdruck bewältigen<br>Selbstsicherer, gelassener &amp; angstfrei werden</p>
      <p>und dabei<br>ein starkes Selbstwertgefühl aufbauen<br>und sich selbst vertrauen</p>
    </div>
    <div class="cover-footer">Einfache Übungen, Techniken und Methoden für den Alltag und ein glückliches erfolgreiches Leben</div>
  </section>

</main>
</body>
</html>
```